VaultMeridan Business Card Re-Design

VaultMeridan is a specialized information security company that applies its proven methodology of security Assessment, Development, Integration and Training (A-D-I-T) to provide cyber security services in the areas of Data Protection, Network Defense and Compliance. We need the current business card re-designed to properly scale the fonts and possibly rearranging some elements (icons, lettering, etc.) to make the card more appealing to the eye. The card should have the logo that is on the web site (www.vaultmeridan-example.com). We would like ideas for both a black card (black background) and a white card (white background). We prefer rounded corners to help the card stand out but are open to all ideas. FYI: VaultMeridan's slogan is "...your security is our business".

Target Market(s)

#1 US Government Contracting Companies, #2 Commercial Companies, #3 Gen. Public.

Industry/Entity Type

Business

Contact Information for Business Card

See Description; open to the use of different fonts.

Font styles to use
Sans Serif

Colors
000000
ec1f27
ffffff

Requirements
Must have
• Company logo on web site, rounded corners, list of company offerings on the back of the card.
Nice to have
• Icons
Should not have
• none

```html
<!DOCTYPE html>
<html lang="en">
<head>
<meta charset="utf-8">
<title>VaultMeridan Business Card</title>
<link href="https://fonts.googleapis.com/css2?family=Open+Sans:wght@400;600;700&display=swap" rel="stylesheet">
<style>
  :root {
    --black: #000000;
    --red: #ec1f27;
    --white: #ffffff;
    --panel-grey: #3a3a3a;
    --panel-grey-dark: #2a2a2a;
    --stage: #e9e9e9;
    --muted: #f2c9a0;
  }
  * { box-sizing: border-box; margin: 0; padding: 0; }
  html, body { width: 1200px; height: 675px; overflow: hidden; }
  body {
    background: var(--stage);
    font-family: "Open Sans", Arial, sans-serif;
    position: relative;
  }
  .card {
    position: absolute;
    top: 160px;
    width: 540px;
    height: 352px;
    background: var(--black);
    border-radius: 12px;
    overflow: hidden;
    color: var(--white);
  }
  .card--front { left: 40px; }
  .card--back { left: 620px; }

  /* Front */
  .brand {
    position: absolute;
    left: 0; top: 0;
    width: 285px; height: 308px;
    display: flex; flex-direction: column; align-items: center; justify-content: center;
    gap: 14px;
  }
  .brand__name {
    font-weight: 700;
    font-size: 28px;
    letter-spacing: 1px;
    color: var(--white);
  }
  .brand__tagline {
    font-size: 11px;
    font-weight: 600;
    color: var(--muted);
  }
  .person {
    position: absolute;
    left: 284px; top: 66px;
    width: 256px; height: 54px;
    background: var(--red);
    padding: 6px 0 0 38px;
  }
  .person__name { font-size: 21px; line-height: 26px; }
  .person__creds { font-size: 9px; margin-left: 4px; }
  .person__title { font-size: 11px; }
  .contact-frame {
    position: absolute;
    left: 284px; top: 120px;
    width: 256px; height: 188px;
  }
  .contact-list {
    position: absolute;
    left: 336px; top: 140px;
    width: 204px; height: 148px;
    background: var(--black);
    list-style: none;
    padding: 10px 0 0 30px;
    display: flex; flex-direction: column; gap: 9px;
  }
  .contact-list li {
    display: flex; align-items: center; gap: 12px;
    font-size: 11.5px; height: 18px;
  }
  .contact-list li.contact--small { font-size: 10.5px; letter-spacing: -0.2px; }
  .contact-list svg { width: 16px; height: 16px; flex: none; }
  .footer {
    position: absolute;
    left: 0; bottom: 0;
    width: 100%; height: 44px;
    background: var(--red);
    display: flex; align-items: center; justify-content: center; gap: 10px;
  }
  .footer__address { font-size: 10.5px; }
  .footer__slogan { font-size: 16px; }

  /* Back */
  .back-brand {
    position: absolute;
    top: 58px; left: 0; width: 100%;
    text-align: center;
    font-weight: 700; font-size: 30px; letter-spacing: 1px;
  }
  .services {
    position: absolute;
    top: 162px;
    list-style: none;
    font-size: 10px; font-weight: 600;
    display: flex; flex-direction: column; gap: 5.5px;
  }
  .services--left { left: 60px; }
  .services--right { left: 306px; }
</style>
</head>
<body>

<section class="card card--front" aria-label="Business card front">
  <div class="brand">
    <span class="brand__name">VaultMeridan</span>
    <span class="brand__tagline">Information Security Solutions</span>
  </div>

  <div class="person">
    <div class="person__name">Darren Holt<span class="person__creds">CISSP, C|EH</span></div>
    <div class="person__title">President - CEO</div>
  </div>

  <svg class="contact-frame" viewBox="0 0 256 188" aria-hidden="true">
    <rect x="0" y="0" width="256" height="188" fill="var(--panel-grey-dark)"/>
    <polygon points="0,0 52,20 52,168 0,188" fill="var(--panel-grey)"/>
  </svg>

  <ul class="contact-list">
    <li>
      <svg viewBox="0 0 16 16"><rect x="5" y="1" width="7" height="14" rx="1.5" fill="var(--red)"/><rect x="6.5" y="3" width="4" height="5" fill="var(--black)"/></svg>
      555.014.2231
    </li>
    <li>
      <svg viewBox="0 0 16 16"><path d="M1 6c0-3 14-3 14 0v1h-4V5H5v2H1z" fill="var(--red)"/><rect x="3" y="8" width="10" height="6" rx="1" fill="none" stroke="var(--red)" stroke-width="1.3"/></svg>
      555.019.4410
    </li>
    <li class="contact--small">
      <svg viewBox="0 0 16 16"><g fill="none" stroke="var(--red)" stroke-width="1.2"><circle cx="8" cy="8" r="6.5"/><ellipse cx="8" cy="8" rx="3" ry="6.5"/><line x1="1.5" y1="8" x2="14.5" y2="8"/></g></svg>
      www.vaultmeridan-example.com
    </li>
    <li class="contact--small">
      <svg viewBox="0 0 16 16"><rect x="1" y="3" width="14" height="10" fill="var(--red)"/><path d="M1 3l7 6 7-6" fill="none" stroke="var(--black)" stroke-width="1.2"/></svg>
      info@vaultmeridan-example.com
    </li>
    <li class="contact--small">
      <svg viewBox="0 0 16 16"><rect x="1" y="3" width="14" height="10" fill="var(--red)"/><path d="M1 3l7 6 7-6" fill="none" stroke="var(--black)" stroke-width="1.2"/></svg>
      dholt@vaultmeridan-example.com
    </li>
  </ul>

  <div class="footer">
    <svg width="12" height="18" viewBox="0 0 12 18" aria-hidden="true"><path d="M6 1a5 5 0 0 0-5 5c0 4 5 11 5 11s5-7 5-11a5 5 0 0 0-5-5z" fill="none" stroke="var(--white)" stroke-width="1.5"/></svg>
    <span class="footer__address">VaultMeridan, Inc. // 412 Harrow Ln. Suite 210 // Easton, Maryland 21601</span>
  </div>
</section>

<section class="card card--back" aria-label="Business card back">
  <div class="back-brand">VaultMeridan</div>

  <ul class="services services--left">
    <li>Secure Cloud &amp; Open Stock Solutions</li>
    <li>Network Attack Penetration &amp; Defense</li>
    <li>Red/Blue Team</li>
    <li>Data Center Consolidation</li>
    <li>Secure Virtual Computing</li>
    <li>Classified Cross Domain Solutions</li>
    <li>Foreign/Counter Intelligence Data Security</li>
  </ul>
  <ul class="services services--right">
    <li>Certification and Accreditation</li>
    <li>Secure Wireless Solutions</li>
    <li>Security Training, Assessment &amp; Integration</li>
    <li>Security Subject Matter Experts</li>
    <li>Executive Security Strategy Coaching</li>
    <li>Data Encryption/Privacy</li>
  </ul>

  <div class="footer">
    <span class="footer__slogan">“Your security is our business.”</span>
  </div>
</section>

</body>
</html>
```